Consulting Group Needs a Graphic Design

We have created a unique, cyclical process to describe our company's philosophy on parenting to our clients. It is provided in the attached file. At the center of the graphic design, which includes all written words on the page, is an image of a gardener that we really like. We found it through a clipart service, but we are not able to trademark it as our own. We would like to create a similar image which includes the female gardener tending the garden, with a trowel in her hand and a watering can at her side. We want the flowers in her garden to be different, just as every child is unique and different within the same family. For more perspective on our company, please visit www.brookvaleguidance.com.
Updates

Project Deadline Extended
Reason: Some of the designers are getting very close to what we want. Due to some unforeseen circumstances, we were unable to give feedback for a couple of days. We would really appreciate your consideration of our request. We are eager to get the design finished to move forward with our branding strategy, so we will be hyper-focused on the project over the coming days. Thank you, Brookvale Family Advisors

Project Deadline Extended
Reason: We would like to give our first choice designer a chance to create a complementary logo to accompany his submission. We have been in communication with this designer.

Industry/Entity Type

Gardener

```html
<!DOCTYPE html>
<html lang="en">
<head>
<meta charset="utf-8">
<title>Every Good Gardener – The Brookvale Growth Method</title>
<link rel="stylesheet" href="https://fonts.googleapis.com/css2?family=Arimo:wght@700&family=Marcellus&display=swap">
<style>
  :root {
    --page: #ffffff;
    --field: #4cb81a;
    --field-glow: #66cc0c;
    --ink-green: #0b3a0b;
    --box-ink: #063806;
    --box-fill: #ffffff;
    --box-border: #cc3300;
    --arrow: #e0542a;
    --scene-leaf: #2f7a12;
    --scene-leaf-dark: #1f5a0c;
    --scene-soil: #6b4214;
  }
  * { margin: 0; padding: 0; box-sizing: border-box; }
  html, body {
    width: 1200px;
    height: 1000px;
    overflow: hidden;
    background: var(--page);
  }
  .canvas {
    position: relative;
    width: 1200px;
    height: 1000px;
    background: var(--page);
  }
  .field {
    position: absolute;
    left: 55px;
    top: 137px;
    width: 1087px;
    height: 818px;
    background: radial-gradient(ellipse at 50% 50%, var(--field-glow) 0%, var(--field) 70%);
  }
  .cycle-art {
    position: absolute;
    left: 0;
    top: 0;
    width: 1200px;
    height: 1000px;
  }
  .cycle-arrow {
    fill: none;
    stroke: var(--arrow);
    stroke-width: 4;
    stroke-linecap: round;
    stroke-linejoin: round;
  }
  .headline {
    font-family: "Marcellus", "Optima", serif;
    font-size: 52px;
    fill: var(--ink-green);
    stroke: var(--ink-green);
    stroke-width: 1.4px;
    letter-spacing: 2px;
  }
  .gardener-scene {
    position: absolute;
    left: 292px;
    top: 458px;
    width: 600px;
    height: 305px;
    border-radius: 48% 48% 42% 42% / 55% 55% 45% 45%;
    background: linear-gradient(180deg, var(--scene-leaf) 0%, var(--scene-leaf-dark) 55%, var(--scene-soil) 100%);
  }
  .method-name {
    position: absolute;
    left: 400px;
    top: 777px;
    width: 350px;
    text-align: center;
    font-family: "Marcellus", serif;
    font-size: 17px;
    letter-spacing: 0.6px;
    color: var(--ink-green);
  }
  .step {
    position: absolute;
    width: 162px;
    height: 103px;
    display: flex;
    align-items: center;
    justify-content: center;
    text-align: center;
    background: var(--box-fill);
    border: 6px solid var(--box-border);
    border-radius: 14px;
    font-family: "Arimo", Arial, sans-serif;
    font-weight: 700;
    font-size: 20px;
    line-height: 1.25;
    color: var(--box-ink);
  }
  .step--plant   { left: 527px; top: 240px; }
  .step--nurture { left: 933px; top: 403px; }
  .step--enrich  { left: 839px; top: 700px; }
  .step--prune   { left: 245px; top: 748px; }
  .step--measure { left: 118px; top: 377px; }
</style>
</head>
<body>
  <main class="canvas">
    <div class="field"></div>

    <svg class="cycle-art" viewBox="0 0 1200 1000">
      <defs>
        <path id="headline-arc" d="M 290 505 A 460 460 0 0 1 900 505"/>
      </defs>

      <g class="cycle-arrows">
        <path class="cycle-arrow" d="M 255 378 C 310 330 400 302 482 297"/>
        <path class="cycle-arrow" d="M 440 282 L 482 297 L 443 330"/>

        <path class="cycle-arrow" d="M 690 300 C 780 310 870 340 918 376"/>
        <path class="cycle-arrow" d="M 895 335 L 918 376 L 868 378"/>

        <path class="cycle-arrow" d="M 1038 508 C 1055 560 1048 620 1012 675"/>
        <path class="cycle-arrow" d="M 1010 628 L 1012 675 L 1052 652"/>

        <path class="cycle-arrow" d="M 840 797 C 720 830 580 835 456 830"/>
        <path class="cycle-arrow" d="M 496 808 L 456 830 L 492 860"/>

        <path class="cycle-arrow" d="M 250 750 C 170 690 120 600 136 515"/>
        <path class="cycle-arrow" d="M 103 535 L 136 515 L 157 545"/>
      </g>

      <text class="headline">
        <textPath href="#headline-arc" startOffset="50%" text-anchor="middle">EVERY GOOD GARDENER:</textPath>
      </text>
    </svg>

    <div class="gardener-scene" role="img" aria-label="Illustration of a woman gardener kneeling in a flower bed with a trowel in her hand, a watering can beside her, shrubs on either side and a different flower for every plant"></div>
    <p class="method-name">The Brookvale Growth Method™</p>

    <div class="step step--plant">Plants with<br>purpose</div>
    <div class="step step--nurture">Nurtures</div>
    <div class="step step--enrich">Enriches<br>the soil</div>
    <div class="step step--prune">Prunes as<br>needed</div>
    <div class="step step--measure">Measures<br>growth</div>
  </main>
</body>
</html>
```